Professional and creatice Life Coach - Business Card design

I just relaunched my website and now i a need a correspoonding business card for my task as life coach. My website is www.tbalrond.com as reference. The compass is kind of a symbol for my work, as I help people navigate through their challenging phases in life. The business card should be colorful, but not too playful as I also adress business people. So it sould be creative, but professional (also to suport my other business as Management Consultant)

Target Market(s)

People who want to get teir problems resolved, in business, partnership and other personal realms

Industry/Entity Type

Life Coaching

Contact Information for Business Card

Front side should include Name, Phone number, Email, Website and address

Font styles to use
Sans Serif

Colors
add136

Requirements
Must have
• "Mag. Leopold Brantner" -> Name
"Energetische Praxis" -> Jobtitle (describing my profession as life coach)
colours and style should match my website www.tbalrond.com
Nice to have
• a compass as a symbol

```html
<!DOCTYPE html>
<html lang="de">
<head>
<meta charset="utf-8">
<title>Visitenkarte – Mag. Leopold Brantner</title>
<link rel="stylesheet" href="https://fonts.googleapis.com/css2?family=Poppins:wght@300;400;600;700&display=swap">
<style>
  :root {
    --lime: #c9df73;
    --lime-soft: #dfeaae;
    --lime-pale: #f1f6e2;
    --charcoal: #3c3e3a;
    --olive-shade: #8a9467;
    --white: #ffffff;
    --page: #ffffff;
  }
  html, body {
    margin: 0;
    padding: 0;
    width: 1200px;
    height: 1200px;
    overflow: hidden;
    background: var(--page);
  }
  .canvas {
    position: relative;
    width: 1200px;
    height: 1200px;
  }
  .business-card {
    position: absolute;
    left: 322px;
    top: 100px;
    width: 555px;
    height: 1000px;
    box-shadow: 6px 8px 10px rgba(0, 0, 0, 0.35);
  }
  .business-card svg {
    display: block;
    width: 100%;
    height: 100%;
  }
  .card-text {
    font-family: "Poppins", sans-serif;
    fill: var(--white);
    text-anchor: middle;
  }
  .card-name { font-size: 12.6px; font-weight: 600; }
  .card-role { font-size: 9px; font-weight: 300; }
  .card-contact { font-size: 10.6px; font-weight: 300; }
  .card-web { font-size: 10px; font-weight: 600; }
  .brand-name {
    font-family: "Poppins", sans-serif;
    font-size: 15px;
    font-weight: 600;
    fill: var(--charcoal);
    text-anchor: middle;
  }
</style>
</head>
<body>
<main class="canvas">
  <article class="business-card">
    <svg viewBox="0 0 314 566" xmlns="http://www.w3.org/2000/svg">
      <defs>
        <linearGradient id="edgeShade" x1="0" y1="0" x2="1" y2="0">
          <stop offset="0" stop-color="#6e7557"/>
          <stop offset="0.7" stop-color="#a9b47e"/>
          <stop offset="1" stop-color="#c9df73"/>
        </linearGradient>
      </defs>

      <rect class="card-base" width="314" height="566" fill="var(--lime)"/>

      <g class="brand-mark">
        <circle cx="157" cy="118" r="60" fill="none" stroke="var(--white)" stroke-width="3.5"/>
        <text class="brand-name" x="157" y="123">Brantner</text>
      </g>

      <path class="wave-shade" d="M25,150 Q120,250 289,272 L289,280 Q130,262 25,160 Z" fill="url(#edgeShade)"/>
      <path class="wave-light" d="M289,168 Q240,232 140,258 Q220,272 289,276 Z" fill="var(--lime-soft)"/>
      <path class="wave-pale" d="M289,194 Q250,242 165,262 Q228,273 289,276 Z" fill="var(--lime-pale)"/>

      <path class="info-panel" d="M25,160 Q130,262 289,276 L289,566 L25,566 Z" fill="var(--charcoal)"/>

      <text class="card-text card-name" x="157" y="322">Mag. Leopold Brantner</text>
      <text class="card-text card-role" x="157" y="352">Energetische Praxis</text>
      <line class="divider" x1="61" y1="392" x2="253" y2="392" stroke="#9a9c96" stroke-width="1"/>
      <text class="card-text card-contact" x="157" y="434">leopold@brantner.one</text>
      <text class="card-text card-contact" x="157" y="479">+43 664 5550182</text>
      <text class="card-text card-web" x="157" y="523">www.tbalrond.com</text>
    </svg>
  </article>
</main>
</body>
</html>
```